New Website design 2024: Harbor Ridge Sealworks, Inc.

1. Who we are: At Harbor Ridge Sealworks Inc, our mission is to provide our clients with comprehensive firestop and seismic expansion joint solutions that ensure the safety and integrity of their buildings. We specialize in the installation of firestop systems at penetrations, wall joints, and slab edge joints, as well as providing acoustical sealants, security sealants, architectural caulking, and seismic expansion joints. Since our establishment in 2007, we have been committed to improving the safety and integrity of buildings through our expertise and use of tested and approved firestop systems. Our focus is to deliver exceptional service and quality workmanship to ensure the protection of lives and property.
2. Services we provide:
-Firestopping: T-ratings, CMU Wall Joint, Exterior Caulking, Fireproof Patching, Head of Wall Joints, Through Penetrations, Curtain Wall/Slab Edge, Grease & Fume Duct Protection.
-Expansion Joints: Floor Covers, Roof Covers, Fire Barriers, Vapor Barriers, Wall & Ceiling Covers, Compression Seals, Pre-Compression Foams, Photoluminescent Signage
3. Examples of scope and projects we’ve completed.
4. How to contact us.: https://harborridgeseal.com/contact/
- Social Media Links: https://www.linkedin.com/company/harbor-ridge-sealworks/mycompany/
https://www.instagram.com/harborridgesealworks/?hl=en
https://www.youtube.com/channel/UCq8Lm2TzR5vKpWd9NhYsJ3b/videos
Target Market(s)
Commercial Construction industry
Industry/Entity Type
Commercial Construction industry in California
Coding
Coded - Design and coding required
Number of Pages Required
4 page
Colors
Designer to choose colors to be used in the design.
Requirements
Must have
- 1. Who we are. 2. Services we provide. 3. Examples of scope and projects we’ve completed. 4. How to contact us.
Nice to have
- Logo. Pictures of scope of work and pictures of projects completed or working on.
Should not have
- Names of clients.

```html
<!DOCTYPE html>
<html lang="en">
<head>
<meta charset="utf-8">
<title>Harbor Ridge Sealworks, Inc.</title>
<link rel="stylesheet" href="https://fonts.googleapis.com/css2?family=Poppins:wght@600;700;800&family=Roboto:wght@400;500;700&display=swap">
<style>
:root{
  --blue:#4059a9;
  --blue-deep:#3a4f9c;
  --red:#e3001b;
  --red-soft:#e8374b;
  --ink:#2b2b2b;
  --muted:#6b6b6b;
  --grey:#f2f2f2;
  --white:#fff;
}
*{box-sizing:border-box;margin:0;padding:0}
html,body{width:1200px;height:4733px;overflow:hidden}
body{position:relative;background:var(--white);font-family:Roboto,sans-serif;color:var(--ink)}
.abs{position:absolute}
.btn{position:absolute;display:flex;align-items:center;justify-content:center;gap:6px;border-radius:26px;color:var(--white);font-size:14px;font-family:Roboto,sans-serif;text-decoration:none}
.arrow{width:14px;height:10px}

/* header */
.site-header{left:0;top:0;width:1200px;height:67px;background:var(--blue);z-index:5}
.brand{left:0;top:0;width:263px;height:67px;background:var(--white);display:flex;align-items:center;gap:8px;padding-left:48px}
.brand-mark{width:14px;height:14px;background:var(--red)}
.brand-name{font-family:Poppins,sans-serif;font-weight:700;font-size:13px;color:var(--red)}
.main-nav a{position:absolute;top:24px;color:var(--white);font-size:14px;font-weight:500;text-decoration:none}
.main-nav .active::after{content:"";position:absolute;left:-14px;right:-14px;top:30px;height:3px;background:var(--red)}
.contact-btn{right:53px;top:8px;width:126px;height:50px;background:var(--red);color:var(--white);font-size:14px;font-weight:500;display:flex;align-items:center;justify-content:center}

/* hero */
.hero{left:0;top:67px;width:1200px;height:633px;background:linear-gradient(135deg,#3d3f46 0%,#55575e 45%,#2f3138 100%);clip-path:polygon(0 0,100% 0,100% 100%,0 82.3%)}
.hero-title{left:0;top:252px;width:1200px;text-align:center;color:var(--white);font-family:Poppins,sans-serif;font-weight:800;font-size:55px;line-height:58px}
.hero-sub{left:0;top:393px;width:1200px;text-align:center;color:var(--white);font-size:16px;line-height:25px}
.hero-btn{left:525px;top:477px;width:150px;height:48px;background:var(--blue)}

/* about */
.eyebrow{color:var(--red);font-size:17px}
.section-title{font-family:Poppins,sans-serif;font-weight:800;color:var(--blue)}
.about-eyebrow{left:46px;top:754px}
.about-title{left:46px;top:778px;font-size:51px;line-height:50px}
.about-text{left:46px;top:900px;width:540px;font-size:15px;line-height:25px;color:var(--muted)}
.about-btn{left:46px;top:1083px;width:173px;height:48px;background:var(--red)}
.about-photo{left:624px;top:751px;width:516px;height:334px;background:linear-gradient(135deg,#b9a999,#9c9a92 50%,#c7cfa0)}

/* services */
.services-band{left:0;top:1186px;width:1200px;height:827px;background:var(--grey);clip-path:polygon(0 13.5%,100% 0,100% 100%,0 86.6%)}
.tile{position:absolute;width:375px;height:234px}
.tile-card{display:flex;flex-direction:column;align-items:center;justify-content:center;text-align:center;padding:0 34px;color:var(--white)}
.tile-card h3{font-size:20px;font-weight:500;margin-bottom:18px}
.tile-card p{font-size:13.5px;line-height:22px}
.tile-red{background:var(--red)}
.tile-blue{background:var(--blue)}
.photo-a{background:linear-gradient(135deg,#a99682,#c6c0a8 55%,#d1d6b0)}
.photo-b{background:linear-gradient(135deg,#c9c6d6,#b3b5c8 50%,#7a85b6)}
.photo-c{background:linear-gradient(135deg,#8c9290,#c9cfd0 50%,#7d8482)}

/* portfolio */
.portfolio-eyebrow{left:0;top:2112px;width:1200px;text-align:center}
.portfolio-title{left:0;top:2132px;width:1200px;text-align:center;font-size:51px}
.filter{position:absolute;top:2211px;height:53px;display:flex;align-items:center;justify-content:center;color:var(--white);font-family:"Roboto Slab",Roboto,serif;font-weight:700;font-size:14px;background:var(--red)}
.filter.active{background:var(--blue)}
.shot{position:absolute;width:346px;height:216px}
.photo-d{background:linear-gradient(135deg,#9a3b34,#c6bcb3 60%,#8e8a85)}
.photo-e{background:linear-gradient(135deg,#d8d5d0,#b8534d 50%,#9ea0a2)}
.photo-f{background:linear-gradient(135deg,#6f7478,#b5b8bb 50%,#d9d6cf)}
.photo-g{background:linear-gradient(135deg,#b9bcc0,#d08d3c 50%,#a8acaf)}

/* testimonials */
.testi-band{left:0;top:3139px;width:1200px;height:822px;background:linear-gradient(160deg,#e3384c,#e02a40 60%,#d92a3e);clip-path:polygon(0 0,100% 13.9%,100% 86.6%,0 100%)}
.testi-title{left:0;top:3330px;width:1200px;text-align:center;color:var(--white);font-family:Poppins,sans-serif;font-weight:700;font-size:32px}
.review{position:absolute;top:3391px;width:334px;height:340px;background:var(--white);text-align:center}
.review svg.quote{position:absolute;left:143px;top:30px}
.review p{position:absolute;left:28px;right:28px;top:100px;font-size:15px;line-height:25px;color:var(--muted)}
.stars{position:absolute;left:0;right:0;top:258px;display:flex;justify-content:center;gap:10px}
.avatar{position:absolute;top:3691px;width:64px;height:64px;border-radius:50%;background:linear-gradient(135deg,#6d7280,#aab0b8);border:2px solid var(--white)}
.reviewer{position:absolute;top:3782px;width:334px;text-align:center;color:var(--white);font-size:16px;font-weight:700}
.testi-btn{left:528px;top:3829px;width:144px;height:46px;background:var(--blue)}

/* partners */
.partner{position:absolute;top:4110px;height:50px;border-radius:4px}

/* footer */
.site-footer{left:0;top:4310px;width:1200px;height:423px;background:var(--blue);clip-path:polygon(0 0,100% 26%,100% 100%,0 100%)}
.foot-brand{left:46px;top:4492px;display:flex;align-items:center;gap:8px}
.foot-brand .brand-mark{width:12px;height:12px}
.foot-brand span{font-family:Poppins,sans-serif;font-weight:700;font-size:13px;color:var(--red)}
.foot-about{left:46px;top:4552px;width:300px;color:var(--white);font-size:14px;line-height:22px}
.foot-col{position:absolute;top:4484px;color:var(--white)}
.foot-col h4{font-family:Poppins,sans-serif;font-weight:700;font-size:19px;margin-bottom:16px}
.foot-col a,.foot-col li{display:block;list-style:none;color:var(--white);text-decoration:none;font-size:14px;line-height:20px;margin-bottom:14px}
.foot-contact li{display:flex;gap:10px;margin-bottom:10px}
.foot-contact svg{flex:none;margin-top:3px}
.copyright{left:0;top:4686px;width:1200px;text-align:center;color:var(--white);font-size:14px}
</style>
</head>
<body>

<header class="site-header abs">
  <div class="brand abs"><span class="brand-mark"></span><span class="brand-name">Harbor Ridge Sealworks</span></div>
  <nav class="main-nav">
    <a class="active" href="#" style="left:453px">Home</a>
    <a href="#" style="left:554px">Who We Are</a>
    <a href="#" style="left:697px">Services</a>
    <a href="#" style="left:815px">Projects</a>
  </nav>
  <a class="contact-btn abs" href="https://harborridgeseal.com/contact/">Contact Us</a>
</header>

<section class="hero abs" role="img" aria-label="Photo of a worker applying firestop sealant on site, darkened"></section>
<h1 class="hero-title abs">Elevating Fire Safety &amp;<br>Structural Integrity</h1>
<p class="hero-sub abs">We are California's Premiere Speciality<br>Firestopping &amp; Seismic Expansion Joint Contractor</p>
<a class="btn hero-btn" href="#"><svg class="arrow" viewBox="0 0 14 10"><path d="M0 5h11M8 1l4 4-4 4" stroke="#fff" stroke-width="2" fill="none"/></svg>Learn More</a>

<p class="eyebrow about-eyebrow abs">About Us</p>
<h2 class="section-title about-title abs">Working Through<br>Dirt &amp; Dust</h2>
<p class="about-text abs">At Harbor Ridge Sealworks Inc, our mission is to provide our clients with comprehensive firestop and seismic expansion joint solutions that ensure the safety and integrity of their buildings. We specialize in the installation of firestop systems at penetrations, wall joints, and slab edge joints, as well as providing acoustical sealants, security sealants, architectural caulking, and seismic expansion joints.</p>
<a class="btn about-btn" href="#"><svg class="arrow" viewBox="0 0 14 10"><path d="M0 5h11M8 1l4 4-4 4" stroke="#fff" stroke-width="2" fill="none"/></svg>More About Us</a>
<div class="about-photo abs" role="img" aria-label="Photo of a worker in a safety vest sealing ductwork above an electrical panel"></div>

<section class="services-band abs"></section>
<div class="tile photo-a" style="left:48px;top:1361px;width:352px" role="img" aria-label="Photo of firestopping work at ductwork"></div>
<div class="tile tile-card tile-red" style="left:412px;top:1361px"><h3>Fireproof Patching</h3><p>Lorem ipsum dolor sit amet, consectetur adipiscing elit, sed do eiusmod tempor incididunt ut labore et dolore.</p></div>
<div class="tile photo-b" style="left:787px;top:1361px;width:376px" role="img" aria-label="Photo of sealed pipe penetrations through a slab"></div>
<div class="tile tile-card tile-blue" style="left:37px;top:1595px"><h3>Head Of Wall Joints</h3><p>Lorem ipsum dolor sit amet, consectetur adipiscing elit, sed do eiusmod tempor incididunt ut labore et dolore.</p></div>
<div class="tile photo-c" style="left:412px;top:1595px" role="img" aria-label="Photo of a sealed curtain wall corner joint"></div>
<div class="tile tile-card tile-blue" style="left:787px;top:1595px;width:376px"><h3>Curtain Wall/Slab Edge</h3><p>Lorem ipsum dolor sit amet, consectetur adipiscing elit, sed do eiusmod tempor incididunt ut labore et dolore.</p></div>

<p class="eyebrow portfolio-eyebrow abs">Portfolio</p>
<h2 class="section-title portfolio-title abs">Our Recent Projects</h2>
<div class="filter active" style="left:276px;width:88px">ALL</div>
<div class="filter" style="left:379px;width:139px">T-RATINGS</div>
<div class="filter" style="left:533px;width:153px">WALL JOINT</div>
<div class="filter" style="left:700px;width:225px">FIREPROOF PATCHING</div>

<div class="shot photo-d" style="left:64px;top:2301px" role="img" aria-label="Project photo of fireproof patching around a box"></div>
<div class="shot photo-a" style="left:428px;top:2301px" role="img" aria-label="Project photo of a worker sealing ductwork"></div>
<div class="shot photo-e" style="left:790px;top:2301px" role="img" aria-label="Project photo of a firestopped cable tray opening"></div>
<div class="shot photo-b" style="left:64px;top:2536px" role="img" aria-label="Project photo of sealed pipe penetrations"></div>
<div class="shot photo-f" style="left:428px;top:2536px" role="img" aria-label="Project photo of a gloved hand sealing a joint"></div>
<div class="shot photo-a" style="left:790px;top:2536px" role="img" aria-label="Project photo of a worker sealing ductwork"></div>
<div class="shot photo-b" style="left:64px;top:2770px" role="img" aria-label="Project photo of sealed pipe penetrations"></div>
<div class="shot photo-g" style="left:428px;top:2770px" role="img" aria-label="Project photo of a worker kneeling at a glass curtain wall"></div>

<section class="testi-band abs" role="img" aria-label="Red toned photo of a worker on site"></section>
<h2 class="testi-title abs">Testimonials</h2>

<div class="review" style="left:85px">
  <svg class="quote" width="48" height="34" viewBox="0 0 48 34"><path d="M2 0h18v18l-9 16H4l7-14H2zM28 0h18v18l-9 16h-7l7-14h-9z" fill="#e3001b"/></svg>
  <p>Aenean eget mollis nisl, ut euismod eros. Duis tincidunt euismod massa eget rutrum. Etiam ac libero vel odio consectetur aliquam malesuada vitae odio. Quisque orci magna.</p>
  <div class="stars"><svg width="106" height="16" viewBox="0 0 106 16"><g fill="#f59a23"><path id="s" d="M8 0l2.4 5 5.6.7-4 3.9 1 5.4L8 12.4 3 15l1-5.4-4-3.9L5.6 5z"/><use href="#s" x="22"/><use href="#s" x="44"/><use href="#s" x="66"/><use href="#s" x="88"/></g></svg></div>
</div>
<div class="review" style="left:434px">
  <svg class="quote" width="48" height="34" viewBox="0 0 48 34"><path d="M2 0h18v18l-9 16H4l7-14H2zM28 0h18v18l-9 16h-7l7-14h-9z" fill="#e3001b"/></svg>
  <p>Aenean eget mollis nisl, ut euismod eros. Duis tincidunt euismod massa eget rutrum. Etiam ac libero vel odio consectetur aliquam malesuada vitae odio. Quisque orci magna.</p>
  <div class="stars"><svg width="106" height="16" viewBox="0 0 106 16"><g fill="#f59a23"><use href="#s"/><use href="#s" x="22"/><use href="#s" x="44"/><use href="#s" x="66"/><use href="#s" x="88"/></g></svg></div>
</div>
<div class="review" style="left:783px">
  <svg class="quote" width="48" height="34" viewBox="0 0 48 34"><path d="M2 0h18v18l-9 16H4l7-14H2zM28 0h18v18l-9 16h-7l7-14h-9z" fill="#e3001b"/></svg>
  <p>Aenean eget mollis nisl, ut euismod eros. Duis tincidunt euismod massa eget rutrum. Etiam ac libero vel odio consectetur aliquam malesuada vitae odio. Quisque orci magna.</p>
  <div class="stars"><svg width="106" height="16" viewBox="0 0 106 16"><g fill="#f59a23"><use href="#s"/><use href="#s" x="22"/><use href="#s" x="44"/><use href="#s" x="66"/><use href="#s" x="88"/></g></svg></div>
</div>
<div class="avatar" style="left:220px" role="img" aria-label="Reviewer portrait"></div>
<div class="avatar" style="left:569px" role="img" aria-label="Reviewer portrait"></div>
<div class="avatar" style="left:918px" role="img" aria-label="Reviewer portrait"></div>
<p class="reviewer" style="left:85px">Marcus Hale</p>
<p class="reviewer" style="left:434px">Devin Ortiz</p>
<p class="reviewer" style="left:783px">Ryan Whitlock</p>
<a class="btn testi-btn" href="#">View More<svg class="arrow" viewBox="0 0 14 10"><path d="M0 5h11M8 1l4 4-4 4" stroke="#fff" stroke-width="2" fill="none"/></svg></a>

<div class="partner" style="left:100px;width:156px;background:#dfe3ee" aria-label="Partner badge"></div>
<div class="partner" style="left:380px;width:156px;background:var(--red)" aria-label="Partner badge"></div>
<div class="partner" style="left:662px;top:4120px;height:28px;width:158px;background:#e8453a" aria-label="Partner badge"></div>
<div class="partner" style="left:943px;width:158px;background:#d9dbe2" aria-label="Partner badge"></div>

<footer class="site-footer abs"></footer>
<div class="foot-brand abs"><span class="brand-mark"></span><span>Harbor Ridge Sealworks</span></div>
<p class="foot-about abs">Lorem ipsum dolor sit amet, consectetur adipiscing elit. Ut elit tellus, luctus nec ullamcorper mattis.</p>
<div class="foot-col" style="left:452px"><h4>Company</h4><a href="#">Home</a><a href="#">About</a><a href="#">Service</a><a href="https://harborridgeseal.com/contact/">Contact</a></div>
<div class="foot-col" style="left:658px"><h4>Further Links</h4><a href="#">Term &amp; Condition</a><a href="#">News</a><a href="#">Recruitment</a></div>
<div class="foot-col foot-contact" style="left:908px;width:250px"><h4>Get In Touch</h4>
  <ul>
    <li><svg width="12" height="14" viewBox="0 0 12 14"><path d="M6 0a5 5 0 0 1 5 5c0 4-5 9-5 9S1 9 1 5a5 5 0 0 1 5-5z" fill="#e3001b"/><circle cx="6" cy="5" r="2" fill="#4059a9"/></svg>2250 E. Marlow Ave Orange, CA 92865</li>
    <li><svg width="12" height="12" viewBox="0 0 12 12"><path d="M2 0l3 3-1.5 2a7 7 0 0 0 3.5 3.5L9 7l3 3-2 2C5 12 0 7 0 2z" fill="#e3001b"/></svg>714-555-0182</li>
    <li><svg width="12" height="12" viewBox="0 0 12 12"><rect x="0" y="1" width="12" height="10" rx="1" fill="#e3001b"/></svg>License #771204</li>
  </ul>
</div>
<p class="copyright abs">Copyright © 2023 Harbor Ridge Sealworks | Powered by Northlane Studio</p>

</body>
</html>
```